Journeys With Marlowe Business Cards

I need a business card design for my upscale Travel Agency.
Attached you can find my logo.
I would like to include the following:
- Name
- Title
- Phone Number
- Email
- Website
- and then something like: Follow us: JourneysWithMarlowe (and then social media icons in color).
The logo should be in the front and then also the back.
I am also attaching a design that I liked (mostly for the layout) but open to any suggestions
Industry/Entity Type
Travel Agent
Contact Information for Business Card
Name: Celine Drummond
Title: Travel Designer / Owner
Phone: 415-296-0487
Email: celine@journeyswithmarlowe.example
Website: www.JourneysWithMarlowe.example
Social Media Handles for FB,IG, Twitter: JourneysWithMarlowe
Font styles to use
Colors
Designer to choose colors to be used in the design.
Look and feel

```html
<!DOCTYPE html>
<html lang="en">
<head>
<meta charset="utf-8">
<title>Journeys With Marlowe – Business Cards</title>
<link rel="stylesheet" href="https://fonts.googleapis.com/css2?family=Open+Sans:wght@400;700&family=Yellowtail&display=swap">
<style>
  :root {
    --backdrop: #262626;
    --card: #ffffff;
    --accent: #f5a95b;
    --accent-deep: #ee9a45;
    --ink: #1c1c1c;
    --social-a: #f5a95b;
    --social-b: #e8894a;
    --social-c: #f7c48e;
  }
  * { box-sizing: border-box; margin: 0; padding: 0; }
  html, body { width: 1200px; height: 900px; overflow: hidden; }
  body {
    background: var(--backdrop);
    font-family: "Open Sans", sans-serif;
    color: var(--ink);
    display: flex;
    flex-direction: column;
    align-items: center;
    justify-content: center;
    gap: 40px;
  }
  .card {
    width: 760px;
    height: 400px;
    background: var(--card);
    position: relative;
    overflow: hidden;
    box-shadow: 0 10px 30px rgba(0,0,0,.45);
  }

  /* brand name block */
  .brand { display: flex; align-items: center; gap: 12px; }
  .brand__mark { width: 26px; height: 26px; background: var(--accent); flex: none; }
  .brand__name { color: var(--accent-deep); font-weight: 700; white-space: nowrap; }

  /* front */
  .card--front .brand { position: absolute; top: 150px; left: 0; right: 0; justify-content: center; }
  .card--front .brand__mark { width: 40px; height: 40px; }
  .card--front .brand__name { font-size: 38px; }
  .website { font-size: 20px; white-space: nowrap; }
  .website strong { color: var(--accent-deep); font-weight: 700; }
  .card--front .website { position: absolute; bottom: 36px; left: 0; right: 0; text-align: center; }

  /* back */
  .card--back .brand { position: absolute; top: 178px; left: 30px; }
  .card--back .brand__mark { width: 22px; height: 22px; }
  .card--back .brand__name { font-size: 20px; }
  .divider { position: absolute; left: 336px; top: 120px; width: 2px; height: 200px; background: var(--accent); }
  .details { position: absolute; left: 356px; top: 112px; width: 384px; }
  .holder-name {
    font-family: "Yellowtail", cursive;
    font-weight: 400;
    color: var(--accent-deep);
    font-size: 42px;
    line-height: 1.1;
    white-space: nowrap;
  }
  .holder-title { font-size: 18px; margin: 4px 0 12px; white-space: nowrap; }
  .contact { list-style: none; font-size: 17px; line-height: 1.5; }
  .contact li { display: flex; align-items: center; gap: 10px; white-space: nowrap; }
  .contact .website { font-size: 17px; }
  .contact svg { width: 17px; height: 17px; flex: none; }
  .social { display: flex; align-items: center; gap: 8px; margin-top: 10px; font-size: 18px; }
  .social__dot { width: 17px; height: 17px; border-radius: 50%; flex: none; }
  .social__dot--a { background: var(--social-a); }
  .social__dot--b { background: var(--social-b); }
  .social__dot--c { background: var(--social-c); }
  .social__handle { margin-left: 8px; white-space: nowrap; }
</style>
</head>
<body>

<section class="card card--front" aria-label="Card front">
  <div class="brand">
    <span class="brand__mark"></span>
    <span class="brand__name">Journeys With Marlowe</span>
  </div>
  <p class="website">www.<strong>JourneysWithMarlowe</strong>.example</p>
</section>

<section class="card card--back" aria-label="Card back">
  <div class="brand">
    <span class="brand__mark"></span>
    <span class="brand__name">Journeys With Marlowe</span>
  </div>
  <div class="divider"></div>
  <div class="details">
    <h1 class="holder-name">Celine Drummond</h1>
    <p class="holder-title">Travel Designer/ Owner</p>
    <ul class="contact">
      <li>
        <svg viewBox="0 0 24 24" fill="none" stroke="#f5a95b" stroke-width="2" stroke-linecap="round" stroke-linejoin="round"><path d="M5 3h4l2 5-2.5 1.5a11 11 0 0 0 6 6L16 13l5 2v4a2 2 0 0 1-2 2A16 16 0 0 1 3 5a2 2 0 0 1 2-2z"/></svg>
        415-296-0487
      </li>
      <li>
        <svg viewBox="0 0 24 24" fill="none" stroke="#f5a95b" stroke-width="2" stroke-linejoin="round"><rect x="3" y="5" width="18" height="14"/><path d="M3 5l9 8 9-8"/></svg>
        celine@journeyswithmarlowe.example
      </li>
      <li>
        <svg viewBox="0 0 24 24" fill="none" stroke="#f5a95b" stroke-width="2"><circle cx="12" cy="12" r="9"/><path d="M3 12h18M12 3c3 3 3 15 0 18M12 3c-3 3-3 15 0 18"/></svg>
        <span class="website">www.<strong>JourneysWithMarlowe</strong>.example</span>
      </li>
    </ul>
    <div class="social">
      <span class="social__dot social__dot--a"></span>
      <span class="social__dot social__dot--b"></span>
      <span class="social__dot social__dot--c"></span>
      <span class="social__handle">JourneysWithMarlowe</span>
    </div>
  </div>
</section>

</body>
</html>
```